New Agency Branding - Logo & Business Card

Project Description

ZUM is a creative agency that crafts memorable product experiences through meaningful design. By channeling the needs of the business and its customers, we are able to construct solutions that are elegant yet effective, powerful yet playful, and familiar yet stimulating.

In addition to our focus towards creating excellent products, we firmly believe that building a strong company culture is paramount. Our values revolve around building an environment that is passionate, supportive, collaborative, curious, humorous, and healthy. The ZUM team is relatively small, and we intend on keep this family tight-knit. We take great care in deciding who we work with and what we work on.

What we’re looking for is a designer who is willing to take on the challenge of helping us visually define and express the ZUM brand. We must comfortably occupy the consumer, commercial, and enterprise sectors. This means looking professional without sacrificing charm. We’re passionate about design and we care about people.

Deliverables

Logo

The first exercise would be to create the ZUM LOGO by referencing the concept that is attached (filename: ZUM Concept Logo). We like the idea of utilizing negative space, but are open to other suggestions. In terms of color, we’ve been flirting with the idea of purple as the primary color, but are again open to other explorations. The logo should be bold, professional, playful, and versatile (it should look just as crisp blown up on a website as it would on a contract).

Accepted Format(s): Adobe Illustrator (.ai) 

Business Card

The second exercise would be to design a business card utilizing the logo. The shape can be standard or square (single our double-sided), and must include the following:

• ZUM LOGO
• Tagline: "human experiences, designed"
• First and Last Name
• Job Role
• Contact Information (email address and phone number)
• Website URL

In terms of typography, we’d like to see considered pairings that compliment the logo, are legible, and can cohesively translate to other mediums (i.e. the ZUM website).

Accepted Format(s): Adobe Photoshop (.psd) OR Adobe Illustrator (.ai)

Style Guide

Finally, we’d like to have the brand defined and presented in a style guide. This would include the full color palette (primary color, secondary color, etc.) and font usage. In addition, we’d like to see rationale clearly communicated for the decisions made.

Visual References

Companies that inspire us:

morrow+venn
http://www.morrowvenn.example/story/morrow-venn/

BRISK
http://www.briskstudio.example

NestHop
https://www.nesthop.example

Fundlark
https://www.fundlark.example

Target Market(s)

Startups, Small to Mid Sized Businesses, Consultant Businesses

Industry/Entity Type

Design Agency

Contact Information for Business Card

FRONT: ZUM LOGO on White background

BACK: Tag line "human experiences, designed", name (i.e. John Doe), job role (i.e. Director, Product Development), phone number, email address, and website. The background color could be a solid color although we are open to suggestions.

Logo Text

ZUM

Font styles to use
Sans Serif

Colors
b768aa
a54499
d2a4cc
876aae
6b449b

Requirements
Must have
• A sense of playfulnesses, charm, excitement, and energy.
• Clean and minimal design
• Avoid using icons for contact information
• NOTE: Not all of the purples that have been chosen must be used. These are only suggestions.

```html
<!DOCTYPE html>
<html lang="en">
<head>
<meta charset="utf-8">
<title>ZUM — Business Card</title>
<link rel="stylesheet" href="https://fonts.googleapis.com/css2?family=Quicksand:wght@500;600;700&display=swap">
<style>
  :root {
    --page-bg: #f1f1f3;
    --brand-purple: #8a66b5;
    --brand-purple-deep: #6b449b;
    --card-light: #e6e7e9;
    --ink: #1c1c1e;
    --ink-soft: #3a3a3d;
    --white: #ffffff;
  }
  * { margin: 0; padding: 0; box-sizing: border-box; }
  html, body {
    width: 1143px;
    height: 1200px;
    overflow: hidden;
    background: var(--page-bg);
    font-family: "Quicksand", sans-serif;
  }
  .stage { position: relative; width: 1143px; height: 1200px; }

  .card {
    position: absolute;
    left: 229px;
    width: 686px;
    height: 394px;
  }
  .card--front { top: 121px; background: var(--brand-purple); }
  .card--back  { top: 626px; background: var(--card-light); }

  .wordmark {
    position: absolute;
    font-family: "Quicksand", sans-serif;
    font-weight: 700;
    line-height: 1;
    letter-spacing: 1px;
    white-space: nowrap;
  }
  .card--front .wordmark {
    left: 0; right: 0;
    top: 115px;
    text-align: center;
    font-size: 100px;
    color: var(--white);
  }
  .tagline {
    position: absolute;
    left: 0; right: 0;
    top: 275px;
    text-align: center;
    font-size: 28px;
    font-weight: 500;
    color: var(--white);
    letter-spacing: 0.3px;
  }

  .card--back .wordmark {
    left: 112px;
    top: 150px;
    font-size: 82px;
    color: var(--brand-purple);
  }
  .divider {
    position: absolute;
    left: 333px;
    top: 103px;
    width: 2px;
    height: 171px;
    background: var(--brand-purple);
  }
  .contact { position: absolute; left: 367px; top: 114px; }
  .contact__name {
    font-size: 25px;
    font-weight: 500;
    color: var(--ink);
    line-height: 1.2;
  }
  .contact__role {
    font-size: 17px;
    font-weight: 600;
    color: var(--brand-purple);
    margin-top: 2px;
  }
  .contact__list { list-style: none; margin-top: 18px; }
  .contact__item {
    font-size: 18px;
    font-weight: 500;
    color: var(--ink-soft);
    line-height: 29px;
    white-space: nowrap;
  }
</style>
</head>
<body>
<main class="stage">
  <section class="card card--front" aria-label="Business card front">
    <div class="wordmark">ZUM</div>
    <p class="tagline">human experiences, designed</p>
  </section>

  <section class="card card--back" aria-label="Business card back">
    <div class="wordmark">ZUM</div>
    <div class="divider"></div>
    <div class="contact">
      <p class="contact__name">Your Name</p>
      <p class="contact__role">Job title</p>
      <ul class="contact__list">
        <li class="contact__item">000 000 0000</li>
        <li class="contact__item">youremail@zumstudio.example</li>
        <li class="contact__item">zumstudio.example</li>
      </ul>
    </div>
  </section>
</main>
</body>
</html>
```